Garten- und Landschaftsbaufirma sucht Design
Zielgruppe
Tätigkeiten der Firma:
- Pflasterarbeiten mit Beton- und Naturstein
- Erdbauarbeiten
- Terrassenbau
- Mauerbau
- Zaun- und Sichtschutzbau
- Rodungen
- Rückschnittarbeiten
- Stauden- und Gehölzpflege
- Baumpflege
- Pflanzungen
- Holzbauarbeiten
- Und noch viele mehr…
Zielgruppe: vermögende Privatkundschaft und Unternehmen
Aufgabenstellung
Erstellung eines unverwechselbaren Logo / Corporate Design sowie einer übersichtlichen Website, die Attribute wie Exklusivität, Leidenschaft, Vertrauen, Qualität, Kreativität, Beharrlichkeit, Ausdauer, Verantwortungsbewusstsein sowie fachliche Kompetenz ausstrahlt.
Design passend zur Lackierung der neuen Firmenfahrzeuge (RAL 6010)
Website wie z.B. die der Firma "Brommelt" .
http://www.brommelt-beispiel.de/start.html

```html
<!DOCTYPE html>
<html lang="de">
<head>
<meta charset="utf-8">
<title>Gartengestaltung Wendrich GmbH</title>
<link href="https://fonts.googleapis.com/css2?family=Mulish:wght@400;500;600&family=Pinyon+Script&display=swap" rel="stylesheet">
<style>
  :root {
    --header-bg: #ffffff;
    --nav-text: #2b2b2b;
    --brand-green: #2f6b3a;
    --menu-orange: #f2a014;
    --menu-text: #1f4a2a;
    --hero-dark: #0f2a33;
    --hero-mid: #1e5560;
    --hero-warm: #b8844a;
    --hero-text: #ffffff;
    --logo-text: #3a3a3a;
  }
  * { margin: 0; padding: 0; box-sizing: border-box; }
  html, body { width: 1200px; height: 675px; overflow: hidden; }
  body { font-family: "Mulish", sans-serif; position: relative; background: var(--hero-dark); }

  .site-header {
    position: absolute; left: 0; top: 0; width: 1200px; height: 97px;
    background: var(--header-bg); z-index: 2;
  }
  .brand {
    position: absolute; left: 26px; top: 20px;
    display: flex; align-items: center; gap: 12px;
  }
  .brand-dot { width: 46px; height: 46px; border-radius: 50%; background: var(--brand-green); }
  .brand-name {
    font-size: 12px; font-weight: 600; line-height: 1.35; letter-spacing: 0.08em;
    color: var(--logo-text); text-transform: uppercase;
  }

  .main-nav { position: absolute; top: 0; left: 0; height: 97px; }
  .nav-item {
    position: absolute; top: 46px; font-size: 21px; font-weight: 500;
    color: var(--nav-text); text-decoration: none; line-height: 1;
  }
  .nav-item.news { left: 368px; }
  .nav-item.team { left: 518px; }
  .nav-item.services {
    left: 613px; top: 40px; width: 164px; height: 57px;
    background: var(--menu-orange); color: var(--menu-text);
    text-align: center; padding-top: 12px;
  }
  .nav-item.services span { border-bottom: 2px solid var(--menu-text); padding-bottom: 2px; }
  .nav-item.references { left: 810px; }
  .nav-item.contact { left: 979px; }

  .services-menu {
    position: absolute; left: 613px; top: 97px; width: 273px; height: 318px;
    background: var(--menu-orange); z-index: 3; list-style: none;
    padding: 10px 0 0 22px;
  }
  .services-menu li {
    font-size: 16.5px; font-weight: 500; color: var(--menu-text);
    line-height: 20px; margin-bottom: 11.5px;
  }

  .hero {
    position: absolute; left: 0; top: 97px; width: 1200px; height: 578px;
    background:
      radial-gradient(ellipse at 35% 30%, rgba(184,132,74,0.55), transparent 45%),
      radial-gradient(ellipse at 85% 35%, rgba(190,110,80,0.45), transparent 40%),
      linear-gradient(180deg, #2d5a78 0%, var(--hero-mid) 45%, var(--hero-dark) 100%);
  }
  .hero-quote {
    position: absolute; left: 55px; top: 315px;
    font-family: "Pinyon Script", cursive; font-size: 60px; line-height: 90px;
    color: var(--hero-text);
  }
  .hero-author {
    position: absolute; left: 466px; top: 488px;
    font-size: 21px; font-weight: 500; color: var(--hero-text);
  }
  .scroll-down { position: absolute; left: 602px; top: 540px; }
</style>
</head>
<body>
  <header class="site-header">
    <div class="brand">
      <div class="brand-dot"></div>
      <div class="brand-name">Gartengestaltung<br>Wendrich GmbH</div>
    </div>
    <nav class="main-nav">
      <a class="nav-item news" href="#">Aktuelles</a>
      <a class="nav-item team" href="#">Team</a>
      <a class="nav-item services" href="#"><span>Leistungen</span></a>
      <a class="nav-item references" href="#">Referenzen</a>
      <a class="nav-item contact" href="#">Kontakt</a>
    </nav>
  </header>

  <ul class="services-menu">
    <li>Pflasterarbeiten mit<br>Beton- und Naturstein</li>
    <li>Erdbauarbeiten</li>
    <li>Terrassenbau</li>
    <li>Mauerbau</li>
    <li>Zaun- und Sichtschutzbau</li>
    <li>Rodungen</li>
    <li>Rückschnittarbeiten</li>
    <li>Stauden- und Gehölzpflege</li>
    <li>Baumpflege</li>
  </ul>

  <section class="hero" role="img" aria-label="Abendliche Villa mit beleuchtetem Pool, Holzdeck und Liegen in tropischem Garten">
    <p class="hero-quote">To plant a garden,<br>is to believe in tomorrow.</p>
    <p class="hero-author">Liselotte Harwig</p>
    <svg class="scroll-down" width="58" height="22" viewBox="0 0 58 22" aria-hidden="true">
      <polyline points="2,2 29,19 56,2" fill="none" stroke="#ffffff" stroke-width="3"/>
    </svg>
  </section>
</body>
</html>
```